Clear Meadow Beauty Product Labels for VERITAS certified skin care products

Design a label template for my certified organic skin care products. I need to be able to edit this label for each product.
Packaging will either be white or black (not yet decided) PET boston bottles ranging from 50mL to 500mL sizes (www.kelbrovessels.com.au), 15mL size Tosni PET bottle (www.marlowsupply.com.au)
Types of products include body wash (500mL), body lotion (500mL), facial cleansers (100mL), face and hand creams (50mL), and eye cream (15mL). More products will be developed such as body scrub, shampoo and conditioner.

Target Market(s)

30 - 55 year old women, middle to high income, living on the Northern Rivers NSW Australia

Industry/Entity Type

Cosmetics

Colors

Designer to choose colors to be used in the design.

Requirements
Must have
• Space on front (or middle if rectangular) of label for product name, volume/mass (note: I need to be able to adjust the size of the volume/mass to suit the packaging, also it needs to be at least 2mm from the limits of the package and separate by at least 2mm in all directions from other graphics), VERITAS ORGANIC logo with SVN bud (products will be certified by Southern Verified Natural (SVN) under the VERITAS standard - refer to SVN labelling attached for VERITAS SVN bud), space for marketing message, and my business logo.
• Space on back (or sides if rectangular) for name and address of company (Clear Meadow Beauty, 17 Brennock Road, Lismore Heights NSW 2480), ingredients list, directions for use, claims of product ('x% organic of total', '100% natural ingredients', I need to be able to add claims for each product), storage, batch number and expiry date, space for safety instructions.
Nice to have
• Simple
• Space on front for picture of key ingredient
• Background a neutral colour
• Use of green and brown colours
Should not have
• Too crowded

```html
<!DOCTYPE html>
<html lang="en">
<head>
<meta charset="utf-8">
<title>Clear Meadow Beauty – Label Range</title>
<link href="https://fonts.googleapis.com/css2?family=Josefin+Sans:wght@300;400;600&family=Libre+Baskerville&display=swap" rel="stylesheet">
<style>
  :root {
    --canvas: #f9f7f6;
    --label-black: #141414;
    --leaf-green: #3b8a2c;
    --white: #ffffff;
    --argan-gold: #b99b5c;
    --soft-grey: #cfcfcf;
  }
  * { box-sizing: border-box; margin: 0; padding: 0; }
  html, body {
    width: 1200px; height: 1153px; overflow: hidden;
    background: var(--canvas);
  }
  .range { position: relative; width: 1200px; height: 1153px; }

  .label {
    position: absolute;
    width: 34.5em;
    background: var(--label-black);
    color: var(--white);
    font-family: "Josefin Sans", sans-serif;
    display: flex; flex-direction: column; align-items: center;
    padding-top: 4.6em;
  }
  .label--body { left: 145px; top: 485px; font-size: 10px; height: 58em; }
  .label--cleanser { left: 615px; top: 655px; font-size: 6.2px; height: 61.5em; }
  .label--eye { left: 942px; top: 873px; font-size: 4.17px; height: 53.7em; }

  .brand { display: flex; align-items: center; gap: 1em; }
  .brand__dot {
    width: 4.6em; height: 4.6em; border-radius: 50%;
    border: 0.25em solid var(--white);
  }
  .brand__name {
    font-size: 2em; font-weight: 400; color: var(--leaf-green);
    line-height: 1.05; letter-spacing: 0.03em;
  }

  .product-name {
    margin-top: 0.9em;
    font-size: 3.8em; font-weight: 300; letter-spacing: 0.02em;
    text-align: center; line-height: 1.05; white-space: nowrap;
  }
  .label--body .product-name { margin-top: 1.3em; }
  .tagline {
    margin-top: 0.9em; font-size: 1.1em; font-weight: 400;
    letter-spacing: 0.08em; text-align: center; line-height: 1.45;
  }
  .label--cleanser .tagline, .label--eye .tagline { color: var(--argan-gold); }
  .key-ingredients {
    margin-top: 2.6em; font-size: 1.15em; letter-spacing: 0.08em;
    color: var(--argan-gold);
  }
  .claim {
    margin-top: 2.2em; font-size: 1.05em; letter-spacing: 0.08em;
    border: 0.1em solid var(--soft-grey); padding: 0.35em 0.6em 0.2em;
  }
  .label--cleanser .claim, .label--eye .claim { margin-top: 1.6em; }

  .key-visual {
    position: absolute; left: 4em; bottom: 10.6em;
    width: 8em; height: 10em;
    background: linear-gradient(160deg, #e9f1f2, #9fb7b9);
    border-radius: 50% 10% 50% 10%;
    opacity: 0.85;
  }
  .certification {
    position: absolute; right: 2.5em; bottom: 10.2em;
    display: flex; flex-direction: column; align-items: center;
  }
  .certification__badge {
    width: 5.8em; height: 3.6em; border-radius: 0.6em;
    border: 0.15em solid var(--white);
  }
  .certification__name {
    margin-top: 0.8em; font-size: 1.45em; text-align: center; line-height: 1.1;
    letter-spacing: 0.03em;
  }

  .volume-band {
    position: absolute; left: 0; right: 0; bottom: 1.4em; height: 7.8em;
    background: var(--leaf-green);
    display: flex; align-items: center; justify-content: center;
  }
  .volume {
    font-family: "Libre Baskerville", serif; font-size: 1.7em; color: var(--white);
  }
</style>
</head>
<body>
<main class="range">

  <section class="label label--body">
    <div class="brand"><span class="brand__dot"></span><span class="brand__name">Clear Meadow Beauty</span></div>
    <h1 class="product-name">BODY LOTION</h1>
    <p class="tagline">LOREM IPSUM DOLOR SIT AMET<br>VET SIT IPSUM LOREM</p>
    <p class="key-ingredients">ARGAN EXTRACT + ALMOND OIL</p>
    <p class="claim">100% NATURAL INGREDIENTS</p>
    <div class="key-visual" role="img" aria-label="Key ingredient illustration: pale leafy sprig"></div>
    <div class="certification">
      <span class="certification__badge"></span>
      <span class="certification__name">VERITAS<br>ORGANIC</span>
    </div>
    <div class="volume-band"><span class="volume">500mL</span></div>
  </section>

  <section class="label label--cleanser">
    <div class="brand"><span class="brand__dot"></span><span class="brand__name">Clear Meadow Beauty</span></div>
    <h1 class="product-name">FACIAL<br>CLEANSER</h1>
    <p class="tagline">LOREM IPSUM DOLOR SIT AMET<br>VET SIT IPSUM LOREM</p>
    <p class="claim">100% NATURAL INGREDIENTS</p>
    <div class="key-visual" role="img" aria-label="Key ingredient illustration: pale leafy sprig"></div>
    <div class="certification">
      <span class="certification__badge"></span>
      <span class="certification__name">VERITAS<br>ORGANIC</span>
    </div>
    <div class="volume-band"><span class="volume">100mL</span></div>
  </section>

  <section class="label label--eye">
    <div class="brand"><span class="brand__dot"></span><span class="brand__name">Clear Meadow Beauty</span></div>
    <h1 class="product-name">EYE<br>CREAM</h1>
    <p class="tagline">LOREM IPSUM DOLOR SIT AMET<br>VET SIT IPSUM LOREM</p>
    <p class="claim">100% NATURAL INGREDIENTS</p>
    <div class="key-visual" role="img" aria-label="Key ingredient illustration: pale leafy sprig"></div>
    <div class="certification">
      <span class="certification__badge"></span>
      <span class="certification__name">VERITAS<br>ORGANIC</span>
    </div>
    <div class="volume-band"><span class="volume">15mL</span></div>
  </section>

</main>
</body>
</html>
```